Tidewell Gearworks LLC

We Need a business card design for a boat/car mechanic. Our thinking is to have Maybe a car on left side of card, boat on the right side of card and diagnostic computer in the middle and a cool creative way to connect all three together. We are also open to other ideas as well!
Would like for back of business card to have the contact info on it “Dorian Vellacott, text is best as the contact method 803-555-0192”

```html
<!DOCTYPE html>
<html lang="en">
<head>
<meta charset="utf-8">
<title>Tidewell Gearworks LLC — Business Card</title>
<link rel="stylesheet" href="https://fonts.googleapis.com/css2?family=Michroma&family=Montserrat:ital,wght@0,400;0,800;1,400&display=swap">
<style>
  :root {
    --canvas: #2b2d31;
    --card-black: #121212;
    --card-light: #e8e8ea;
    --brand-red: #e3202a;
    --ink-dark: #151515;
    --ink-light: #ffffff;
    --sea-blue: #3f6f86;
    --hull-white: #e9ecef;
    --screen-blue: #1f6fc4;
    --car-gold: #c9952e;
  }
  * { box-sizing: border-box; margin: 0; padding: 0; }
  html, body { width: 1200px; height: 985px; overflow: hidden; }
  body {
    background: var(--canvas);
    display: flex;
    flex-direction: column;
    align-items: center;
    justify-content: center;
    gap: 56px;
  }
  .card {
    position: relative;
    width: 680px;
    height: 389px;
    border-radius: 22px;
    overflow: hidden;
    box-shadow: 0 10px 30px rgba(0,0,0,.45);
  }

  /* Front */
  .card--front { background: var(--card-black); }
  .card--front .art { position: absolute; inset: 0; width: 100%; height: 100%; }
  .brand {
    position: absolute;
    display: flex;
    align-items: center;
    gap: 22px;
  }
  .card--front .brand { right: 40px; top: 50%; transform: translateY(-50%); }
  .brand__mark {
    width: 64px; height: 64px;
    border-radius: 50%;
    background: var(--brand-red);
    flex: none;
  }
  .brand__rule { width: 2px; height: 110px; background: var(--brand-red); flex: none; }
  .brand__name {
    font-family: "Michroma", sans-serif;
    font-size: 25px;
    line-height: 1.22;
    letter-spacing: 1px;
    text-transform: uppercase;
  }
  .card--front .brand__name { color: var(--ink-light); }

  /* Back */
  .card--back { background: var(--card-light); }
  .card--back .brand { left: 50%; top: 62px; transform: translateX(-42%); }
  .card--back .brand__name { color: var(--ink-dark); font-size: 27px; }
  .card--back .brand__mark { width: 70px; height: 70px; }
  .contact {
    position: absolute;
    left: 0; right: 0;
    top: 232px;
    text-align: center;
    color: var(--ink-dark);
  }
  .contact__name {
    font-family: "Montserrat", sans-serif;
    font-weight: 800;
    font-size: 21px;
    letter-spacing: 1.5px;
    text-transform: uppercase;
  }
  .contact__underline {
    width: 190px; height: 2px;
    background: var(--brand-red);
    margin: 10px auto 12px;
  }
  .contact__line {
    font-family: "Michroma", sans-serif;
    font-size: 15px;
    letter-spacing: .3px;
  }
  .contact__phone { font-weight: 700; }
</style>
</head>
<body>

  <section class="card card--front" aria-label="Card front">
    <svg class="art" viewBox="0 0 680 389" preserveAspectRatio="none" aria-hidden="false">
      <defs>
        <linearGradient id="servicesGradient" x1="0" y1="0" x2="1" y2="1">
          <stop offset="0" stop-color="var(--sea-blue)"/>
          <stop offset="0.32" stop-color="var(--hull-white)"/>
          <stop offset="0.55" stop-color="#f4f4f4"/>
          <stop offset="0.72" stop-color="#dfe3e8"/>
          <stop offset="1" stop-color="var(--car-gold)"/>
        </linearGradient>
      </defs>
      <polygon class="services-photo" points="0,0 300,0 410,389 0,389" fill="url(#servicesGradient)"
               role="img" aria-label="Photo collage: a white motor boat on the water, a diagnostic computer workstation, and a white sports car with gold wheels"/>
      <polygon class="accent-stripe" points="300,0 312,0 422,389 410,389" fill="var(--brand-red)"/>
    </svg>
    <div class="brand">
      <span class="brand__mark"></span>
      <span class="brand__rule"></span>
      <p class="brand__name">Tidewell<br>Gearworks<br>LLC</p>
    </div>
  </section>

  <section class="card card--back" aria-label="Card back">
    <div class="brand">
      <span class="brand__mark"></span>
      <span class="brand__rule"></span>
      <p class="brand__name">Tidewell<br>Gearworks<br>LLC</p>
    </div>
    <div class="contact">
      <p class="contact__name">Dorian Vellacott</p>
      <div class="contact__underline"></div>
      <p class="contact__line">text is best as the contact method <span class="contact__phone">803-555-0192</span></p>
    </div>
  </section>

</body>
</html>
```